Letterhead Design for Law Firm that Specializes in Property Damage Litigation

We are looking for a redesign of our letterhead. Our current letterhead lists all of our current staff members and we'd like to come up with a design that does NOT list all of the staff members so that it does not need to be updated with every newly hired employee. Must be in editable format.

We are a law firm that specializes in property damage, so we need something that is professional, yet modern. The final design should use our existing logo and should use a blue color scheme (alternate colors would be gray, black, and white).

Industry/Entity Type

Legal

Colors
0054AA
0677BA
7BADD7
CADEEF
E8F1F8

```html
<!DOCTYPE html>
<html lang="en">
<head>
<meta charset="utf-8">
<title>Hartwell Ames &amp; Corbin — Letterhead</title>
<link href="https://fonts.googleapis.com/css2?family=Barlow:wght@400;500;600&family=Roboto:wght@400;500;700&family=Roboto+Condensed:wght@400;700&display=swap" rel="stylesheet">
<style>
  :root {
    --navy: #0f2a63;
    --navy-bar: #243f7a;
    --brand-blue: #0054aa;
    --rule-blue: #0677ba;
    --ink: #2b2b2b;
    --grey: #555b63;
    --backdrop: #d9d9d9;
    --paper: #ffffff;
  }
  * { margin: 0; padding: 0; box-sizing: border-box; }
  html, body {
    width: 1200px; height: 1200px; overflow: hidden;
    background: var(--backdrop);
  }
  .letterhead {
    position: absolute; left: 200px; top: 34px;
    width: 800px; height: 1132px;
    background: var(--paper);
    font-family: "Barlow", sans-serif;
    color: var(--ink);
  }
  .masthead {
    position: absolute; top: 40px; left: 0; width: 100%;
    text-align: center;
  }
  .firm-name {
    display: inline-flex; align-items: center; gap: 12px;
    font-family: "Barlow", sans-serif; font-weight: 600;
    font-size: 27px; letter-spacing: 1.5px; text-transform: uppercase;
    color: var(--navy); line-height: 1;
  }
  .firm-mark { width: 16px; height: 16px; background: var(--navy); }
  .tagline {
    margin: 26px auto 0; width: 266px;
    font-family: "Roboto", sans-serif; font-weight: 500;
    font-size: 10px; letter-spacing: 2.6px; color: var(--grey);
    padding-bottom: 6px; border-bottom: 1px solid var(--rule-blue);
  }
  .contact-line {
    margin-top: 5px;
    font-family: "Roboto", sans-serif; font-size: 14px; color: var(--grey);
    display: flex; justify-content: center; align-items: center; gap: 6px;
  }
  .contact-line svg { width: 10px; height: 10px; fill: var(--navy); }
  .contact-line .domain { color: var(--navy); font-weight: 700; }
  .letter {
    position: absolute; left: 63px; width: 674px;
    font-size: 14px; letter-spacing: 0.5px;
  }
  .recipient { top: 226px; line-height: 18px; }
  .salutation { top: 352px; }
  .body-copy { top: 397px; line-height: 23.4px; text-align: justify; }
  .closing { top: 747px; }
  .signature {
    position: absolute; left: 58px; top: 780px;
    width: 330px; height: 62px;
    background: linear-gradient(90deg, #e9e9e9, #f4f4f4);
  }
  .offices {
    position: absolute; left: 63px; top: 1070px;
    font-family: "Roboto Condensed", sans-serif; font-size: 9.5px;
    line-height: 17px; color: var(--ink);
  }
  .offices .label { font-weight: 700; color: var(--navy); }
  .offices .address { color: var(--navy); }
  .base-bar {
    position: absolute; left: 0; bottom: 0; width: 100%; height: 13px;
    background: var(--navy-bar);
  }
</style>
</head>
<body>
  <main class="letterhead">
    <header class="masthead">
      <div class="firm-name"><span class="firm-mark"></span>Hartwell Ames &amp; Corbin</div>
      <p class="tagline">THE PROPERTY DAMAGE ATTORNEYS</p>
      <p class="contact-line">
        <svg viewBox="0 0 10 10"><path d="M2 0.5 L3.6 2.6 L2.8 3.6 C3.4 5 4.8 6.4 6.3 7.1 L7.3 6.3 L9.5 7.9 L8.4 9.5 C4.5 9.2 0.8 5.5 0.5 1.6 Z"/></svg>
        555.014.2200 &nbsp;|&nbsp;
        <svg viewBox="0 0 10 10"><circle cx="5" cy="5" r="4.5"/></svg>
        <span>www.<span class="domain">hacpropertylaw</span>.com</span>
      </p>
    </header>

    <address class="letter recipient" style="font-style:normal">
      Mr. John Doe<br>President<br>Strategy Accountants<br>111 Street Name,<br>City State, 12345
    </address>

    <p class="letter salutation">Dear :</p>

    <div class="letter body-copy">
      <p>Lorem ipsum dolor sit amet, consectetur adipiscing elit. Aenean ut ipsum eget massa hendrerit vestibulum vel in velit. Donec pretium neque velit.</p>
      <p>Aliquam porta lectus nec mauris ornare venenatis. Vivamus non est turpis, et cursus sem. Mauris vehicula erat in diam auctor at bibendum nisl lacinia.</p>
      <p>Morbi imperdiet neque vehicula nunc convallis gravida. Vestibulum iaculis pretium placerat. Integer consequat, est sit amet facilisis eleifend, nibh nibh varius orci, eget dapibus arcu dui non purus. Pellentesque in magna mauris. Duis enim sapien, dictum vitae condimentum a, pulvinar vel lacus. Mauris et molestie nibh. Vestibulum vitae nulla at metus elementum porta sit amet interdum elit. Nulla sollicitudin neque eu nulla volutpat congue.</p>
      <p>Etiam pellentesque, velit id dapibus fermentum, turpis sapien ornare dui, ac tincidunt ligula odio congue purus. Nunc sed ante dui, in porta lectus. Cras nec sem lorem. In hac habitasse platea dictumst. Maecenas id diam quis dui porta tristique. Sed id egestas felis. Donec ullamcorper mattis posuere. Phasellus fermentum eleifend tortor vel dapibus. Vestibulum ante ipsum.</p>
    </div>

    <p class="letter closing">Sincerely Yours</p>
    <div class="signature" role="img" aria-label="Handwritten signature of Daniel R. Voss"></div>

    <footer class="offices">
      <p><span class="label">RIVERTON OFFICE :</span> &#9742; 555.014.2200 &nbsp; &#9113; 555.014.2290 &nbsp;| &nbsp;<span class="address">420 Market Row, Suite 810 Riverton, PA 19000</span></p>
      <p><span class="label">MAPLE GROVE OFFICE :</span> &#9742; 555.018.3310 &nbsp;| &#9113; 555.014.2290 | &nbsp;<span class="address">75 Orchard Lane Suite 300, Maple Grove, NJ 08000</span></p>
    </footer>

    <div class="base-bar"></div>
  </main>
</body>
</html>
```